International online gaming platform needs a game UI design

1. We need a game interface for three kinds of theme based on our guideline and sample mockup.
2. The product type is the online casino games related, we need a series of casino games UIs, however, we can start on the game lobby first.
3. Three theme you might choose from or refer to:
A. 3D look & feel
B. Realistic casino theme
C. Richness and grandeur
D. European casino style
4. NOT ALLOWED to change the design layout.
MUST follow our sample mock up and ONLY redefine the design style.
5. All items must be in a stand-alone component, eg. Button, Tab, Icon,... etc.
6. We need the layout in vector shape, but we can review in JPG or PNG format.
7. The image size: 1366 x 768

Updated:
1. All items and their positions should be same as the sample UI we provided.
Please redesign all the items and create a new theme for it.
No need to create a new layout.
2. Although we accept the draft design, but all the items in UI should be completed.
3. All the wordings in the sample UI are confirmed, you might change the fonts.
4. For the avatar in the left hand side, you don't have to redraw it.
We already have our own avatar system implemented.
5. All the items such as icons, tabs, and buttons are free to redesign.

Dear designers,

We've increased our budget and raise the prize money to 800 USD.  
We also accept the draft design in PNG format and we can go through the details in handover stage.
Thank you very much. 

Reason: Dear designers, We decided to extend the deadline by 7 days. As mentioned in the task description, we are looking for a new style of design and you might refer to the below style. A. 3D look & feel B. Realistic casino theme C. Richness and grandeur D. European casino style If you are still interested in our project, please send us your work. Thank you very much!

Casino

```html
<!DOCTYPE html>
<html lang="en">
<head>
<meta charset="utf-8">
<title>Casino Lobby UI Kit</title>
<link rel="stylesheet" href="https://fonts.googleapis.com/css2?family=Arimo:wght@400;700&display=swap">
<style>
:root{
  --page:#ffffff;
  --brown-hi:#8a4a33;
  --brown-lo:#3f1f14;
  --brown-edge:#2c1a12;
  --gold-hi:#ffe55a;
  --gold-mid:#f7b400;
  --gold-lo:#e58400;
  --gold-edge:#f1c21b;
  --red-hi:#ff8a2a;
  --red-lo:#d92a00;
  --ink:#ffffff;
  --ink-dark:#3a2410;
  --panel-black:#0b0b0b;
  --deal-red:#a3232b;
  --bead-blue:#1c3f8f;
  --bead-red:#d4202a;
  --avatar-hi:#3d8fe0;
  --avatar-lo:#0b3f8f;
  --cell-grey:#dadada;
  --icon-hi:#d9d2cc;
  --icon-lo:#8c7a6e;
}
*{box-sizing:border-box;margin:0;padding:0}
html,body{width:1200px;height:823px;overflow:hidden;background:var(--page)}
body{font-family:"Arimo",Arial,sans-serif}
.canvas{position:relative;width:1200px;height:823px;overflow:hidden}

/* game tabs */
.tab{position:absolute;height:42px;width:281px;border-radius:5px 5px 2px 2px;
  border:2px solid var(--brown-edge);
  background:linear-gradient(180deg,var(--brown-hi),#5e2d1d 55%,var(--brown-lo));
  color:var(--ink);font-weight:700;font-size:24px;line-height:38px;padding-left:97px}
.tab--active{height:51px;line-height:54px;border-color:var(--gold-edge);
  background:linear-gradient(180deg,var(--gold-hi),var(--gold-mid) 55%,var(--gold-lo))}
.tab--narrow{padding-left:91px}
.tab--narrower{padding-left:87px}
.tab-icon{position:absolute;left:8px;top:-8px;width:58px;height:56px;border-radius:8px;
  background:linear-gradient(180deg,var(--icon-hi),var(--icon-lo))}
.tab--active .tab-icon{top:-3px}

/* toolbars */
.toolbar{position:absolute;left:50px;width:226px;height:45px;background:var(--panel-black);
  display:flex;gap:11px;padding:8px 0 0 17px}
.tool{width:30px;height:30px;border:1px solid #fff4a0;border-radius:2px;
  background:linear-gradient(180deg,var(--gold-hi),var(--gold-mid) 60%,var(--gold-lo));
  display:flex;align-items:center;justify-content:center}
.toolbar--hot .tool{border-color:#ffb070;background:linear-gradient(180deg,var(--red-hi),var(--red-lo))}
.tool svg{width:22px;height:22px;fill:none;stroke:#4a2a00;stroke-width:2.2}
.toolbar--hot .tool svg{stroke:#5a0f00}

/* panels */
.panel{position:absolute;border-radius:10px}
.panel--brown{background:linear-gradient(180deg,#8a4a2c,#5a2c1a);border-radius:10px 10px 0 0}
.panel--black{background:var(--panel-black);border:5px solid #6d6d6d;border-radius:14px;box-shadow:inset 0 0 0 2px #d8d8d8}
.panel--grey{background:linear-gradient(180deg,#5a5a5a,#333);border-radius:10px 10px 0 0}

/* dealer cards */
.dealer-card{position:absolute;display:grid;padding:3px;gap:4px 5px;border-radius:4px;
  background:linear-gradient(180deg,#707070,#2a2a2a);border:1px solid #9a9a9a}
.dealer-card--sm{width:260px;height:118px;grid-template-columns:81px 1fr;grid-template-rows:82px 1fr}
.dealer-card--lg{grid-template-columns:101px 1fr;grid-template-rows:106px 1fr;
  background:linear-gradient(180deg,#fff2a0,var(--gold-mid));border:2px solid #7a4a10}
.avatar{border:2px solid #c9a15a;border-radius:2px;
  background:radial-gradient(circle at 50% 45%,var(--avatar-hi),var(--avatar-lo))}
.road{background-color:#fff;border:1px solid #bbb;
  background-image:conic-gradient(var(--cell-grey) 25%,#fff 0 50%,var(--cell-grey) 0 75%,#fff 0);
  background-size:var(--cell2) var(--cell2);position:relative}
.dealer-card--sm .road{--cell:11.5px;--cell2:23px}
.dealer-card--lg .road{--cell:13px;--cell2:26px}
.beads{position:absolute;left:1px;top:1px;display:grid;grid-template-columns:repeat(5,var(--cell))}
.bead{width:var(--cell);height:var(--cell);border-radius:50%;border:2px solid var(--bead-blue);background:#fff}
.bead--red{border-color:var(--bead-red)}
.name-bar{grid-column:1/3;display:flex;align-items:center;justify-content:space-between;
  background:var(--panel-black);border:1px solid #e6e6e6;border-radius:2px;color:var(--ink);padding-left:7px}
.dealer-card--sm .name-bar{font-size:13px}
.dealer-card--lg .name-bar{font-size:16px}
.deals{background:var(--deal-red);height:100%;display:flex;align-items:center;padding:0 5px 0 8px}

/* control bars */
.bar{position:absolute;height:48px;border-radius:6px;border:2px solid #2a1810;
  background:linear-gradient(180deg,#7a4a33,#3a1f14)}
.mode-btn{position:absolute;left:5px;top:5px;width:170px;height:36px;border-radius:4px;
  border:1px solid #ffe27a;background:linear-gradient(180deg,#ffd84a,var(--gold-lo));
  color:var(--ink);font-weight:700;font-size:13px;display:flex;align-items:center;gap:10px;padding-left:6px}
.mode-btn .badge{width:24px;height:24px;border-radius:3px;background:#fff3b0;display:flex;align-items:center;justify-content:center}
.mode-slot{position:absolute;left:179px;top:5px;right:3px;height:36px;border-radius:4px;
  background:linear-gradient(180deg,#6a3d28,#3a2014);border:1px solid #2a1810}
.filters{position:absolute;left:7px;top:7px;display:flex;gap:3px}
.filter{height:32px;display:flex;align-items:center;justify-content:center;gap:4px;
  font-size:18px;color:var(--ink-dark);border-radius:2px;
  background:linear-gradient(180deg,#5a3a10,#c9951e 22%,#f3c84a 50%,#b07a15 82%,#4a2c0a)}
.filter--small{font-size:16px}
.filter svg{fill:var(--ink-dark)}
.gap-left{margin-left:5px}
</style>
</head>
<body>
<main class="canvas">

  <!-- game tabs -->
  <nav class="tabs">
    <div class="tab" style="left:14px;top:14px"><span class="tab-icon" role="img" aria-label="Baccarat game icon"></span>Bacarat</div>
    <div class="tab tab--narrow" style="left:299px;top:14px"><span class="tab-icon" role="img" aria-label="Super six game icon"></span>Super six</div>
    <div class="tab tab--narrower" style="left:585px;top:14px"><span class="tab-icon" role="img" aria-label="Roulette game icon"></span>Roulette</div>
    <div class="tab tab--narrower" style="left:871px;top:14px"><span class="tab-icon" role="img" aria-label="Sic Bo game icon"></span>Sic Bo</div>

    <div class="tab tab--active" style="left:14px;top:102px"><span class="tab-icon" role="img" aria-label="Baccarat game icon"></span>Bacarat</div>
    <div class="tab tab--active tab--narrow" style="left:299px;top:102px"><span class="tab-icon" role="img" aria-label="Super six game icon"></span>Super six</div>
    <div class="tab tab--active tab--narrower" style="left:585px;top:102px"><span class="tab-icon" role="img" aria-label="Roulette game icon"></span>Roulette</div>
    <div class="tab tab--active tab--narrower" style="left:871px;top:102px"><span class="tab-icon" role="img" aria-label="Sic Bo game icon"></span>Sic Bo</div>
  </nav>

  <!-- toolbars -->
  <div class="toolbar" style="top:216px">
    <span class="tool"><svg viewBox="0 0 24 24"><circle cx="10" cy="10" r="6.5"/><path d="M15 15l6 6M10 6.5v7M12 8h-3a1.2 1.2 0 0 0 0 2.4h2a1.2 1.2 0 0 1 0 2.4H8"/></svg></span>
    <span class="tool"><svg viewBox="0 0 24 24"><circle cx="10" cy="10" r="6.5"/><path d="M15 15l6 6M7 10h6"/></svg></span>
    <span class="tool"><svg viewBox="0 0 24 24"><path d="M8 18V5l11-2v13"/><circle cx="6" cy="18" r="2.5"/><circle cx="17" cy="16" r="2.5"/></svg></span>
    <span class="tool"><svg viewBox="0 0 24 24"><path d="M3 8V3h5M16 3h5v5M21 16v5h-5M8 21H3v-5M3 3l6 6M21 3l-6 6M21 21l-6-6M3 21l6-6"/></svg></span>
    <span class="tool"><svg viewBox="0 0 24 24"><path d="M5 5l14 14M19 5L5 19" stroke-width="3"/></svg></span>
  </div>
  <div class="toolbar toolbar--hot" style="top:269px">
    <span class="tool"><svg viewBox="0 0 24 24"><circle cx="10" cy="10" r="6.5"/><path d="M15 15l6 6M10 6.5v7M12 8h-3a1.2 1.2 0 0 0 0 2.4h2a1.2 1.2 0 0 1 0 2.4H8"/></svg></span>
    <span class="tool"><svg viewBox="0 0 24 24"><circle cx="10" cy="10" r="6.5"/><path d="M15 15l6 6M7 10h6"/></svg></span>
    <span class="tool"><svg viewBox="0 0 24 24"><path d="M8 18V5l11-2v13"/><circle cx="6" cy="18" r="2.5"/><circle cx="17" cy="16" r="2.5"/></svg></span>
    <span class="tool"><svg viewBox="0 0 24 24"><path d="M3 8V3h5M16 3h5v5M21 16v5h-5M8 21H3v-5M3 3l6 6M21 3l-6 6M21 21l-6-6M3 21l6-6"/></svg></span>
    <span class="tool"><svg viewBox="0 0 24 24"><path d="M5 5l14 14M19 5L5 19" stroke-width="3"/></svg></span>
  </div>

  <!-- lobby state: first table selected -->
  <section class="lobby-state">
    <div class="panel panel--brown" style="left:10px;top:336px;width:339px;height:172px"></div>
    <div class="dealer-card dealer-card--lg" style="left:18px;top:346px;width:316px;height:145px">
      <div class="avatar" role="img" aria-label="Dealer avatar placeholder"></div>
      <div class="road"><div class="beads"><span class="bead"></span><span class="bead bead--red"></span><span class="bead bead--red"></span><span class="bead bead--red"></span><span class="bead"></span><span class="bead"></span><span class="bead bead--red"></span></div></div>
      <div class="name-bar"><span>Dealer Name</span><span class="deals">Deals 999</span></div>
    </div>

    <div class="panel panel--black" style="left:359px;top:344px;width:832px;height:151px"></div>
    <div class="dealer-card dealer-card--sm" style="left:379px;top:361px">
      <div class="avatar" role="img" aria-label="Dealer avatar placeholder"></div>
      <div class="road"><div class="beads"><span class="bead"></span><span class="bead bead--red"></span><span class="bead bead--red"></span><span class="bead bead--red"></span><span class="bead"></span><span class="bead"></span><span class="bead bead--red"></span></div></div>
      <div class="name-bar"><span>Dealer Name</span><span class="deals">Deals 999</span></div>
    </div>
    <div class="dealer-card dealer-card--sm" style="left:646px;top:361px">
      <div class="avatar" role="img" aria-label="Dealer avatar placeholder"></div>
      <div class="road"><div class="beads"><span class="bead"></span><span class="bead bead--red"></span><span class="bead bead--red"></span><span class="bead bead--red"></span><span class="bead"></span><span class="bead"></span><span class="bead bead--red"></span></div></div>
      <div class="name-bar"><span>Dealer Name</span><span class="deals">Deals 999</span></div>
    </div>
    <div class="dealer-card dealer-card--sm" style="left:912px;top:361px">
      <div class="avatar" role="img" aria-label="Dealer avatar placeholder"></div>
      <div class="road"><div class="beads"><span class="bead"></span><span class="bead bead--red"></span><span class="bead bead--red"></span><span class="bead bead--red"></span><span class="bead"></span><span class="bead"></span><span class="bead bead--red"></span></div></div>
      <div class="name-bar"><span>Dealer Name</span><span class="deals">Deals 999</span></div>
    </div>

    <div class="bar" style="left:10px;top:508px;width:538px">
      <div class="mode-btn"><span class="badge"><svg width="18" height="18" viewBox="0 0 18 18" fill="#d88a00"><circle cx="6" cy="5" r="3"/><circle cx="12" cy="8" r="3"/><path d="M1 16c0-4 2-6 5-6s5 2 5 6zM8 17c0-3 2-5 4-5s5 2 5 5z"/></svg></span>Multiplayer</div>
      <div class="mode-slot"></div>
    </div>
    <div class="bar" style="left:557px;top:508px;width:641px">
      <div class="filters">
        <span class="filter" style="width:133px">Join any</span>
        <span class="filter filter--small" style="width:54px">A➔Z</span>
        <span class="filter" style="width:54px">$<svg width="12" height="16" viewBox="0 0 12 16"><path d="M3 0h6v9h3l-6 7-6-7h3z"/></svg></span>
        <span class="filter" style="width:54px">$<svg width="12" height="16" viewBox="0 0 12 16"><path d="M3 16h6V7h3L6 0 0 7h3z"/></svg></span>
        <span class="filter gap-left" style="width:55px"><svg width="30" height="16" viewBox="0 0 30 16"><circle cx="6" cy="4" r="3"/><circle cx="15" cy="4" r="3"/><circle cx="24" cy="4" r="3"/><path d="M0 16c0-5 2-8 6-8s6 3 6 8zM9 16c0-5 2-8 6-8s6 3 6 8zM18 16c0-5 2-8 6-8s6 3 6 8z"/></svg></span>
        <span class="filter" style="width:53px">&lt;3</span>
        <span class="filter" style="width:54px">&gt;3</span>
        <span class="filter" style="width:134px">All Limits <svg width="14" height="10" viewBox="0 0 14 10"><path d="M0 0h14L7 9z"/></svg></span>
      </div>
    </div>
  </section>

  <!-- lobby state: second table selected -->
  <section class="lobby-state">
    <div class="panel panel--grey" style="left:0;top:607px;width:277px;height:150px"></div>
    <div class="dealer-card dealer-card--sm" style="left:10px;top:624px">
      <div class="avatar" role="img" aria-label="Dealer avatar placeholder"></div>
      <div class="road"><div class="beads"><span class="bead"></span><span class="bead bead--red"></span><span class="bead bead--red"></span><span class="bead bead--red"></span><span class="bead"></span><span class="bead"></span><span class="bead bead--red"></span></div></div>
      <div class="name-bar"><span>Dealer Name</span><span class="deals">Deals 999</span></div>
    </div>

    <div class="panel panel--brown" style="left:283px;top:601px;width:338px;height:167px"></div>
    <div class="dealer-card dealer-card--lg" style="left:290px;top:608px;width:325px;height:148px">
      <div class="avatar" role="img" aria-label="Dealer avatar placeholder"></div>
      <div class="road"><div class="beads"><span class="bead"></span><span class="bead bead--red"></span><span class="bead bead--red"></span><span class="bead bead--red"></span><span class="bead"></span><span class="bead"></span><span class="bead bead--red"></span></div></div>
      <div class="name-bar"><span>Dealer Name</span><span class="deals">Deals 999</span></div>
    </div>

    <div class="panel panel--black" style="left:633px;top:608px;width:572px;height:150px"></div>
    <div class="dealer-card dealer-card--sm" style="left:646px;top:625px">
      <div class="avatar" role="img" aria-label="Dealer avatar placeholder"></div>
      <div class="road"><div class="beads"><span class="bead"></span><span class="bead bead--red"></span><span class="bead bead--red"></span><span class="bead bead--red"></span><span class="bead"></span><span class="bead"></span><span class="bead bead--red"></span></div></div>
      <div class="name-bar"><span>Dealer Name</span><span class="deals">Deals 999</span></div>
    </div>
    <div class="dealer-card dealer-card--sm" style="left:912px;top:625px">
      <div class="avatar" role="img" aria-label="Dealer avatar placeholder"></div>
      <div class="road"><div class="beads"><span class="bead"></span><span class="bead bead--red"></span><span class="bead bead--red"></span><span class="bead bead--red"></span><span class="bead"></span><span class="bead"></span><span class="bead bead--red"></span></div></div>
      <div class="name-bar"><span>Dealer Name</span><span class="deals">Deals 999</span></div>
    </div>

    <div class="bar" style="left:0;top:772px;width:548px">
      <div class="mode-btn" style="left:12px"><span class="badge"><svg width="18" height="18" viewBox="0 0 18 18" fill="#d88a00"><circle cx="6" cy="5" r="3"/><circle cx="12" cy="8" r="3"/><path d="M1 16c0-4 2-6 5-6s5 2 5 6zM8 17c0-3 2-5 4-5s5 2 5 5z"/></svg></span>Multiplayer</div>
      <div class="mode-slot" style="left:189px"></div>
    </div>
    <div class="bar" style="left:557px;top:772px;width:641px">
      <div class="filters">
        <span class="filter" style="width:133px">Join any</span>
        <span class="filter filter--small" style="width:54px">A➔Z</span>
        <span class="filter" style="width:54px">$<svg width="12" height="16" viewBox="0 0 12 16"><path d="M3 0h6v9h3l-6 7-6-7h3z"/></svg></span>
        <span class="filter" style="width:54px">$<svg width="12" height="16" viewBox="0 0 12 16"><path d="M3 16h6V7h3L6 0 0 7h3z"/></svg></span>
        <span class="filter gap-left" style="width:55px"><svg width="30" height="16" viewBox="0 0 30 16"><circle cx="6" cy="4" r="3"/><circle cx="15" cy="4" r="3"/><circle cx="24" cy="4" r="3"/><path d="M0 16c0-5 2-8 6-8s6 3 6 8zM9 16c0-5 2-8 6-8s6 3 6 8zM18 16c0-5 2-8 6-8s6 3 6 8z"/></svg></span>
        <span class="filter" style="width:53px">&lt;3</span>
        <span class="filter" style="width:54px">&gt;3</span>
        <span class="filter" style="width:134px">All Limits <svg width="14" height="10" viewBox="0 0 14 10"><path d="M0 0h14L7 9z"/></svg></span>
      </div>
    </div>
  </section>

</main>
</body>
</html>
```